Talvern Asset Management - Corporate Letter Head Project

Looking for a classy design based on our current logo. Please find current logo source file in files. With our color scheme.

Target Market(s)

We're an investment firm, the letterhead needs to look professional and attractive to clients.

Industry/Entity Type

Hedgefund

Colors
0054AA
0677BA
7BADD7
CADEEF
E8F1F8

Requirements
Must have
• Our logo, address, phone number, and email

```html
<!DOCTYPE html>
<html lang="en">
<head>
<meta charset="utf-8">
<title>Talvern Asset Management – Letterhead</title>
<link rel="stylesheet" href="https://fonts.googleapis.com/css2?family=Cormorant+Garamond:wght@600&family=Open+Sans:wght@400&display=swap">
<style>
  :root {
    --navy: #1f2b4a;
    --backdrop: #c9c9c9;
    --paper: #ffffff;
    --ink: #1f2b4a;
  }
  * { box-sizing: border-box; margin: 0; padding: 0; }
  html, body {
    width: 1200px; height: 686px; overflow: hidden;
    background: var(--backdrop);
  }
  .letterhead {
    position: absolute;
    left: 374px; top: 23px;
    width: 452px; height: 640px;
    background: var(--paper);
    box-shadow: 0 6px 24px rgba(0,0,0,0.25);
    overflow: hidden;
  }
  .brand {
    position: absolute; left: 36px; top: 42px;
    display: flex; align-items: center; gap: 10px;
  }
  .brand-square {
    width: 30px; height: 30px;
    border: 1.5px solid var(--navy);
  }
  .brand-name {
    font-family: "Cormorant Garamond", serif;
    font-weight: 600; color: var(--ink);
    font-size: 19px; line-height: 1; letter-spacing: 0.5px;
  }
  .brand-name .sub {
    display: block; font-size: 8.5px; letter-spacing: 5.2px;
    margin-top: 3px;
  }
  .contact {
    position: absolute; left: 262px; top: 34px;
    padding-left: 12px;
    border-left: 1.2px solid var(--navy);
    font-family: "Open Sans", sans-serif;
    font-size: 7.6px; line-height: 1.35; color: var(--ink);
  }
  .contact-row { display: flex; gap: 6px; align-items: flex-start; margin-bottom: 2px; }
  .contact-row svg { width: 8px; height: 8px; flex: none; margin-top: 1px; fill: var(--navy); }
  .footer-wave { position: absolute; left: 0; bottom: 0; width: 452px; height: 160px; }
</style>
</head>
<body>
  <main class="letterhead">
    <header>
      <div class="brand">
        <span class="brand-square"></span>
        <div class="brand-name">TALVERN ASSET<span class="sub">MANAGEMENT</span></div>
      </div>
      <address class="contact" style="font-style:normal">
        <div class="contact-row">
          <svg viewBox="0 0 10 10"><path d="M5 0a3.5 3.5 0 0 0-3.5 3.5C1.5 6 5 10 5 10s3.5-4 3.5-6.5A3.5 3.5 0 0 0 5 0zm0 5a1.5 1.5 0 1 1 0-3 1.5 1.5 0 0 1 0 3z"/></svg>
          <span>27 Harrowden Lane<br>Ashford, Kent, TN23 4QX</span>
        </div>
        <div class="contact-row">
          <svg viewBox="0 0 10 10"><path d="M2 0.5l2 2-1 1.3c.6 1.3 1.7 2.4 3 3l1.3-1 2 2L8 9.5C4 9.5 0.5 6 0.5 2z"/></svg>
          <span>(555) 018-4426</span>
        </div>
        <div class="contact-row">
          <svg viewBox="0 0 10 10"><circle cx="5" cy="5" r="4.3" fill="none" stroke="#1f2b4a" stroke-width="1.2"/><path d="M0.7 5h8.6M5 .7c-2.4 2.6-2.4 6 0 8.6M5 .7c2.4 2.6 2.4 6 0 8.6" fill="none" stroke="#1f2b4a" stroke-width=".8"/></svg>
          <span>www.talvernam.com</span>
        </div>
        <div class="contact-row">
          <svg viewBox="0 0 10 10"><path d="M0.5 2h9v6h-9z" fill="none" stroke="#1f2b4a" stroke-width="1"/><path d="M0.5 2l4.5 3.5L9.5 2" fill="none" stroke="#1f2b4a" stroke-width="1"/></svg>
          <span>info@talvernam.com</span>
        </div>
      </address>
    </header>

    <svg class="footer-wave" viewBox="0 0 452 160" preserveAspectRatio="none" aria-hidden="true">
      <path d="M0 160 L0 150 C120 140 210 126 280 88 C340 54 390 18 452 8 L452 160 Z" fill="var(--navy)"/>
      <path d="M6 138 C120 128 205 112 272 76 C330 44 385 8 452 0" fill="none" stroke="var(--navy)" stroke-width="2"/>
    </svg>
  </main>
</body>
</html>
```